Lorcan Webpage Design

I would like to start an business and management consultancy business. I am thinking to called it "Movara Consultancy". Besides the consultancy services, I would also like to provide training on finance, forensic accounting, fraud prevention and internal control.
Professional management consultants are contracted by organizations to provide advisory services in an objective and independent manner.

Services include, but are not limited to, strategic planning, facilitation, quality assurance, education and training, investment counsel, identification and analysis of management problems, developing solutions, and the implementation of proposed solutions.

Professional management consultants are hired when an organization lacks sufficient resources, requires external objective advice, or because they have expertise not available within the client organization.

I would like to see the webpage design that use colors apple green with some other contrast color. The design have to be professional look but with a new age touch.

Reason: Unable to find a suitable web pages design

Dear all

Since last week I post a request, but till to date, I has yet to received a new sparkling creative and "wow" web page design. Please help me here!

Regards

Reason: Yet to found a suitable web designer for my web design. Help! I just need a fresh and professional look design. You may ignore the color code I prefer. Send me your sparkling creative work. Thank you so much!

Some examples

```html
<!DOCTYPE html>
<html lang="en">
<head>
<meta charset="utf-8">
<title>Movara Consultancy</title>
<link rel="stylesheet" href="https://fonts.googleapis.com/css2?family=Arimo:wght@400;700&display=swap">
<style>
  :root {
    --apple: #33d011;
    --apple-bright: #1ef000;
    --apple-pale: #d6f9d2;
    --forest: #0f4a00;
    --ink: #000000;
    --paper: #ffffff;
    --footer: #05050a;
  }
  * { box-sizing: border-box; margin: 0; padding: 0; }
  html, body { width: 1188px; height: 1200px; overflow: hidden; }
  body {
    position: relative;
    font-family: "Arimo", Arial, sans-serif;
    color: var(--ink);
    background: var(--forest);
  }
  .site-header {
    position: absolute; left: 0; top: 0; width: 1188px; height: 153px;
    background: var(--apple);
  }
  .brand {
    position: absolute; left: 41px; top: 64px;
    font-size: 42px; font-weight: 400; color: var(--paper); letter-spacing: 0.5px;
  }
  .contact-link {
    position: absolute; right: 12px; top: 70px;
    display: flex; align-items: center; gap: 10px;
    font-size: 27px; color: var(--ink);
  }
  .main-nav {
    position: absolute; left: 0; top: 153px; width: 1188px; height: 70px;
    display: flex;
    background: linear-gradient(to bottom, #ffffff 0%, #dffcd8 35%, #5ef23c 80%, var(--apple-bright) 100%);
  }
  .nav-item {
    display: flex; align-items: center; justify-content: center;
    font-size: 33px; border-left: 1px solid #1a5c0a;
  }
  .nav-item:first-child { border-left: none; }
  .hero {
    position: absolute; left: 0; top: 223px; width: 1188px; height: 491px;
    background:
      radial-gradient(ellipse 55% 60% at 50% 35%, #d8ff9a 0%, #8fe63a 35%, #3fb018 70%, #1d6a08 100%);
  }
  .welcome-card {
    position: absolute; left: 20px; top: 738px; width: 833px; height: 304px;
    border-radius: 34px;
    background: linear-gradient(to bottom, var(--apple-pale) 0%, #8ff87a 45%, var(--apple-bright) 100%);
    padding: 12px 0 0 18px;
  }
  .welcome-title { text-align: center; font-size: 26px; font-weight: 700; padding-right: 18px; }
  .intro-heading { font-size: 27px; font-weight: 700; margin-top: 18px; }
  .intro-text { font-size: 27px; line-height: 34px; word-break: break-all; margin-top: 2px; }
  .news-card {
    position: absolute; left: 891px; top: 735px; width: 289px; height: 303px;
    border-radius: 22px;
    background: linear-gradient(to bottom, #dff5dc 0%, #8ff07a 45%, var(--apple-bright) 100%);
    padding: 18px 20px 0 20px;
  }
  .news-title { text-align: center; font-size: 27px; font-weight: 700; }
  .news-lead { font-size: 27px; margin-top: 14px; }
  .news-line { height: 34px; border-bottom: 2px solid var(--ink); }
  .site-footer {
    position: absolute; left: 0; top: 1141px; width: 1188px; height: 59px;
    background: var(--footer); color: var(--paper);
    display: flex; align-items: center; justify-content: center;
    font-size: 27px;
  }
</style>
</head>
<body>
  <header class="site-header">
    <div class="brand">MOVARA CONSULTANCY</div>
    <div class="contact-link">
      <svg width="38" height="32" viewBox="0 0 38 32" aria-hidden="true">
        <rect x="1" y="1" width="36" height="30" rx="3" fill="#e8e070" stroke="#9a8f20" stroke-width="2"/>
        <polyline points="3,5 19,18 35,5" fill="none" stroke="#9a8f20" stroke-width="2"/>
      </svg>
      <span>Contact Us</span>
    </div>
  </header>

  <nav class="main-nav">
    <div class="nav-item" style="width:144px">
      <svg width="70" height="50" viewBox="0 0 70 50" aria-label="Home">
        <polygon points="35,2 2,28 10,28 35,9 60,28 68,28" fill="#0f4a00"/>
        <polygon points="13,26 35,10 57,26 57,49 42,49 42,34 28,34 28,49 13,49" fill="#0f4a00"/>
        <rect x="50" y="5" width="7" height="14" fill="#0f4a00"/>
      </svg>
    </div>
    <div class="nav-item" style="width:162px">About</div>
    <div class="nav-item" style="width:183px">Traning</div>
    <div class="nav-item" style="width:224px">Services</div>
    <div class="nav-item" style="width:241px">Education</div>
    <div class="nav-item" style="width:234px">Facilitation</div>
  </nav>

  <div class="hero" role="img" aria-label="Business people in silhouette shaking hands in front of a green world map"></div>

  <section class="welcome-card">
    <h1 class="welcome-title">WELCOME TO OUR COMPANY</h1>
    <h2 class="intro-heading">INTRODUCTION :</h2>
    <p class="intro-text">&nbsp;“ Your introduction Your introduction Your introduction Your introduction Your introduction Your introduction Your introduction Your introduction ....</p>
  </section>

  <aside class="news-card">
    <h2 class="news-title">Company News</h2>
    <p class="news-lead">Today Our News is</p>
    <div class="news-line"></div>
    <div class="news-line"></div>
    <div class="news-line"></div>
    <div class="news-line"></div>
  </aside>

  <footer class="site-footer">All Right Reserved Copyright 2013</footer>
</body>
</html>
```